Tranquil Pathway Business Card

Logo attached. (will be printing onto thick white/off white textured card)

Double sided business card for two Therapists working at Tranquil Pathway.

Require one design, but with different name and mobile numbers on each card.

Target Market(s)

Medical, Health

Industry/Entity Type

Business

Contact Information for Business Card

Need one business card design, but a separate card for each person - Colin Marchetti and Marieke de Boeckx.

FRONT OF CARD

Logo

Name (Colin Marchetti on one card, Marieke de Boeckx on the other)
Professional Clinical Hypnotherapist

Consulting Rooms (Near Lindqvist Hospital)
482 Brackenfield Road
Dunmore VIC 3987

Colin@TranquilPathway.example.au OR Marieke@TranquilPathway.example.au

Mobile: 0455 872 604 (for Colin) OR
Mobile: 0467 290 518 (for Marieke)

BACK OF CARD

Logo

Website: www.TranquilPathway.example.au

Phone: 1300 958 471

Requirements
Must have
• Text and logo only. No additiional graphics.

```html
<!DOCTYPE html>
<html lang="en">
<head>
<meta charset="utf-8">
<title>Tranquil Pathway – Business Card</title>
<link href="https://fonts.googleapis.com/css2?family=Raleway:wght@300;400;700&display=swap" rel="stylesheet">
<style>
  :root {
    --navy: #2b2f5e;
    --grey: #6b6b6b;
    --rule: #7a7a7a;
    --paper: #ffffff;
  }
  html, body {
    margin: 0;
    padding: 0;
    overflow: hidden;
    background: var(--paper);
  }
  .card {
    position: relative;
    width: 686px;
    height: 1200px;
    background: var(--paper);
    font-family: "Raleway", sans-serif;
    overflow: hidden;
  }
  .rule {
    position: absolute;
    left: 43px;
    width: 600px;
    height: 2px;
    background: var(--rule);
  }
  .rule--top { top: 43px; }
  .rule--middle { top: 820px; }
  .rule--bottom { top: 1167px; }

  .brand-mark {
    position: absolute;
    left: 45px;
    top: 140px;
  }
  .brand-divider {
    position: absolute;
    left: 250px;
    top: 148px;
    width: 3px;
    height: 176px;
    background: var(--grey);
  }
  .brand-name {
    position: absolute;
    left: 274px;
    color: var(--navy);
    font-weight: 700;
    line-height: 1;
    white-space: nowrap;
  }
  .brand-name--primary {
    top: 198px;
    font-size: 58px;
    letter-spacing: 1px;
  }
  .brand-name--secondary {
    top: 256px;
    font-size: 29px;
    letter-spacing: 10px;
  }

  .line {
    position: absolute;
    left: 0;
    width: 686px;
    text-align: center;
    line-height: 1;
    white-space: nowrap;
  }
  .person-name {
    top: 425px;
    font-size: 56px;
    font-weight: 700;
    color: var(--navy);
  }
  .person-name .particle {
    font-size: 40px;
  }
  .person-role {
    font-size: 34px;
    font-weight: 400;
    color: var(--grey);
    letter-spacing: 3px;
  }
  .person-role--first { top: 488px; }
  .person-role--second { top: 535px; }

  .mobile {
    top: 651px;
    font-size: 35px;
    color: var(--grey);
    font-weight: 400;
  }
  .mobile .label {
    color: var(--navy);
    font-weight: 700;
  }
  .email {
    top: 695px;
    font-size: 26px;
    color: var(--grey);
    font-weight: 400;
  }
  .email .label {
    color: var(--navy);
    font-weight: 700;
  }

  .rooms-heading {
    top: 921px;
    font-size: 46px;
    font-weight: 700;
    color: var(--navy);
  }
  .rooms-line {
    font-size: 32px;
    font-weight: 400;
    color: var(--grey);
    letter-spacing: 2px;
  }
  .rooms-line--1 { top: 971px; }
  .rooms-line--2 { top: 1010px; }
  .rooms-line--3 { top: 1049px; }
</style>
</head>
<body>
  <main class="card">
    <div class="rule rule--top"></div>

    <header class="brand">
      <svg class="brand-mark" width="192" height="192" viewBox="0 0 192 192" aria-hidden="true">
        <circle cx="96" cy="96" r="92" fill="var(--navy)"/>
      </svg>
      <div class="brand-divider"></div>
      <div class="brand-name brand-name--primary">TRANQUIL</div>
      <div class="brand-name brand-name--secondary">PATHWAY</div>
    </header>

    <section class="person">
      <div class="line person-name">MARIEKE <span class="particle">DE</span> BOECKX</div>
      <div class="line person-role person-role--first">PROFESSIONAL CLINICAL</div>
      <div class="line person-role person-role--second">HYPNOTHERAPIST</div>
      <div class="line mobile"><span class="label">MOBILE</span> | 0467 290 518</div>
      <div class="line email"><span class="label">MARIEKE</span>@TranquilPathway.example.au</div>
    </section>

    <div class="rule rule--middle"></div>

    <section class="rooms">
      <div class="line rooms-heading">CONSULTING ROOMS</div>
      <div class="line rooms-line rooms-line--1">(NEAR LINDQVIST HOSPITAL)</div>
      <div class="line rooms-line rooms-line--2">482 BRACKENFIELD ROAD</div>
      <div class="line rooms-line rooms-line--3">DUNMORE VIC 3987</div>
    </section>

    <div class="rule rule--bottom"></div>
  </main>
</body>
</html>
```